Marlowe Fen Gin (bottle label)

Marlowe Fen Gin is a hand crafted spirit distilled by Tidewell Distillery. The distillery is farm based. This is our first offering. The label is to be applied to a glass bottle.

We chose the name because we felt lucky to chance upon a great recipe. So we came up with Marlowe Fen Gin. The phrase "Sometimes you get lucky" needs to be included. We'd like to see imagery of a lucky symbol such as a 4 leaf clover or shooting star. Elegant contrast come to mind. Reference to the distillery, bottle size (375ml) and Alc./vol. 40% is also needed. The distillery logo could be included. Or all is included in printed content.
Logo included for reference.
The label is rectangular.

Target Market(s)

Adults who enjoy fine spirits

Industry/Entity Type

Spirits distillation

Font styles to use
Serif
Script

Requirements
Must have
• classy, eye catching presentation
Nice to have
• Stylized 4 leaf clover or shooting star
Should not have
• Nothing hokey

```html
<!DOCTYPE html>
<html lang="en">
<head>
<meta charset="utf-8">
<title>Marlowe Fen Gin – Bottle Label</title>
<link rel="stylesheet" href="https://fonts.googleapis.com/css2?family=Oswald:wght@500;600&family=Righteous&display=swap">
<style>
  :root {
    --backdrop: #0e1413;
    --teal: #52d4c8;
    --teal-deep: #3cbdb2;
    --silver: #d6dbe3;
    --silver-dark: #5f6777;
    --seal-red: #e8353c;
    --seal-text: #ffe9e6;
  }
  * { margin: 0; padding: 0; box-sizing: border-box; }
  html, body { width: 1200px; height: 1200px; overflow: hidden; background: var(--backdrop); }
  .canvas { position: relative; width: 1200px; height: 1200px; }

  .label {
    position: absolute; left: 150px; top: 100px;
    width: 900px; height: 1000px;
    background: var(--teal);
  }
  .label::before, .label::after {
    content: ""; position: absolute; left: 0; width: 100%; height: 16px;
    background: radial-gradient(circle at 50% 100%, var(--teal) 13px, transparent 14px) repeat-x;
    background-size: 30px 16px;
  }
  .label::before { top: -15px; }
  .label::after { bottom: -15px; transform: scaleY(-1); }

  .slogan {
    position: absolute; top: 50px; width: 100%; text-align: center;
    font: 600 54px/1 "Oswald", sans-serif; letter-spacing: 1px;
    color: var(--silver-dark); text-transform: uppercase;
  }

  .emblem { position: absolute; left: 0; top: 110px; width: 900px; height: 640px; }
  .emblem-title { font-family: "Righteous", sans-serif; font-size: 92px; fill: var(--silver); letter-spacing: 4px; }
  .emblem-gin { font-family: "Righteous", sans-serif; font-size: 170px; fill: var(--silver); letter-spacing: 10px; }

  .info {
    position: absolute; font: 600 34px/1.05 "Oswald", sans-serif;
    text-transform: uppercase; color: var(--silver-dark);
  }
  .info--left { left: 40px; top: 790px; }
  .info--right { right: 40px; top: 790px; text-align: left; color: var(--silver); }
  .info small { display: block; font-size: 28px; }

  .seal {
    position: absolute; left: 330px; top: 735px; width: 240px; height: 240px;
    border-radius: 50%; background: var(--seal-red);
    display: flex; align-items: center; justify-content: center; text-align: center;
    font: 600 32px/1.1 "Oswald", sans-serif; color: var(--seal-text); text-transform: uppercase;
  }

  .volume, .strength {
    position: absolute; top: 918px; font: 600 28px/1 "Oswald", sans-serif; color: var(--silver-dark);
  }
  .volume { left: 40px; }
  .strength { right: 40px; color: var(--silver); }
</style>
</head>
<body>
<main class="canvas">
  <section class="label">
    <p class="slogan">Sometimes you get lucky</p>

    <svg class="emblem" viewBox="0 0 900 640" aria-labelledby="emblem-name">
      <title id="emblem-name">Marlowe Fen Gin</title>
      <defs>
        <radialGradient id="burst-tone" cx="50%" cy="50%" r="50%">
          <stop offset="0%" stop-color="#e9eef3" stop-opacity="0.85"/>
          <stop offset="45%" stop-color="#b7e9e3" stop-opacity="0.5"/>
          <stop offset="100%" stop-color="#52d4c8" stop-opacity="0"/>
        </radialGradient>
        <radialGradient id="clover-tone" cx="50%" cy="50%" r="50%">
          <stop offset="0%" stop-color="#aab2c0"/>
          <stop offset="100%" stop-color="#6e7789"/>
        </radialGradient>
        <path id="title-arc" d="M 195 300 A 255 255 0 0 1 705 300"/>
      </defs>
      <circle cx="450" cy="300" r="320" fill="url(#burst-tone)" role="img" aria-label="Silver sunburst rays radiating from the centre"/>
      <circle cx="450" cy="300" r="95" fill="url(#clover-tone)" role="img" aria-label="Stylised silver four-leaf clover"/>
      <text class="emblem-title" text-anchor="middle">
        <textPath href="#title-arc" startOffset="50%">MARLOWE FEN</textPath>
      </text>
      <text class="emblem-gin" x="450" y="555" text-anchor="middle">GIN</text>
    </svg>

    <p class="info info--left">Hand crafted<small>in small batches</small></p>
    <div class="seal">Tidewell<br>Distillery</div>
    <p class="info info--right">With organic<small>farm ingredients</small></p>

    <p class="volume">37.5cl/375ml</p>
    <p class="strength">40% alc./vol.</p>
  </section>
</main>
</body>
</html>
```